Web form face-lift for an online startup

We are a web startup building a SaaS application for the freight industry. The project is mainly dedicated to the paint the main form that our customer are using along the search results that the they get. All details are in the attached documents.
Updates
The application serves the Freight Forwarders community so please think towards this industry when using background images, banners, colors, icons, etc. Computer and technology images are irrelevant.
Customer fields at the top of the page is actually part of the form.
Target Market(s)
Usually business users (Sales people, procurement, shippers, freight forwarders). Some are less tech savvy and some appreciate the new trendy web apps.
Industry/Entity Type
Building
Colors
Designer to choose colors to be used in the design.
Look and feel
Each slider illustrates characteristics of the customer's brand and the style your logo design should communicate.

```html
<!DOCTYPE html>
<html lang="en">
<head>
<meta charset="utf-8">
<title>Cargoway – Search For Quotes</title>
<link href="https://fonts.googleapis.com/css2?family=Roboto:wght@300;400;500;700&family=Roboto+Slab:wght@700&display=swap" rel="stylesheet">
<style>
  :root{
    --blue:#3a9ad9;
    --blue-dark:#2b86c5;
    --blue-deep:#2a7fbf;
    --white:#ffffff;
    --ink:#444a50;
    --ink-soft:#666d73;
    --line:#d8dde1;
    --grey:#8e9396;
    --grey-btn:#9a9fa2;
    --footer:#a7a9ab;
    --footer-ink:#6f7376;
    --red:#d7262c;
  }
  *{box-sizing:border-box;margin:0;padding:0}
  html,body{width:1200px;height:921px;overflow:hidden;background:var(--white)}
  body{font-family:"Roboto",sans-serif;color:var(--ink);position:relative}
  .abs{position:absolute}
  .site-header{position:absolute;left:0;top:0;width:1200px;height:58px;background:var(--blue);border-bottom:3px solid var(--blue-dark)}
  .brand{left:170px;top:20px;font-family:"Roboto",sans-serif;font-weight:700;font-size:22px;color:var(--white);letter-spacing:.5px}
  .nav-item{top:27px;font-size:12.5px;color:var(--white)}
  .meta{top:7px;font-size:9.5px;color:var(--white)}
  .user{left:911px;top:26px;font-size:12.5px;font-weight:500;color:var(--white);display:flex;align-items:center;gap:6px}
  .hero{left:0;top:58px;width:1200px;height:289px;background:linear-gradient(180deg,#3c3f4a 0%,#6a5a5e 30%,#d27a4c 52%,#3d3030 70%,#1c1d24 100%)}
  .hero-title{left:173px;top:145px;font-size:19px;color:var(--white)}
  .label-light{color:var(--white);font-size:12.5px}
  .customer-input{left:240px;top:178px;width:212px;height:28px;background:var(--white);border:1px solid #ddd}
  .check{width:12px;height:12px;background:#f2f2f2;border:1px solid #b8bcbf;border-radius:2px}
  .tab{background:var(--white);display:flex;align-items:center;justify-content:center}
  .tab.active{background:var(--blue)}
  .form-band{left:0;top:347px;width:1200px;height:133px;background:var(--blue)}
  .f-label{top:368px;font-size:13px;color:var(--white)}
  .f-input{top:394px;height:28px;border:1px solid var(--white);color:var(--white);font-size:12.5px;display:flex;align-items:center;justify-content:center}
  .f-select{top:394px;height:28px;background:var(--white);border:1px solid var(--white);color:var(--ink);font-size:12.5px;display:flex;align-items:center;padding-left:9px}
  .unit{top:394px;height:28px;background:var(--grey-btn);color:var(--white);font-size:14px;font-weight:500;display:flex;align-items:center}
  .unit span{flex:1;padding-left:11px}
  .unit i{width:26px;height:100%;border-left:1px solid #b5b9bb;display:flex;align-items:center;justify-content:center}
  .add-units{left:170px;top:438px;width:127px;height:24px;background:var(--grey-btn);color:var(--white);font-size:12px;font-weight:500;display:flex;align-items:center;gap:10px;padding-left:8px}
  .route{left:0;top:482px;width:1200px;height:52px;border-bottom:1px solid var(--line)}
  .r-label{top:502px;font-size:12px;font-weight:500;color:var(--ink)}
  .r-input{top:493px;height:31px;border:1px solid #bfc4c8;font-size:12px;color:var(--ink-soft);display:flex;align-items:center;padding-left:10px}
  .options-title{left:169px;top:577px;font-size:19px;font-weight:300;color:var(--ink)}
  .opt{top:627px;font-size:14px;font-weight:300;color:var(--ink)}
  .opt a{color:var(--blue);text-decoration:none}
  .sep{top:629px;width:0;height:13px;border-left:1px dotted #999}
  .price{left:678px;top:618px;width:353px;height:34px;border:1px solid #bfc4c8;font-size:13.5px;font-weight:300;display:flex;align-items:center;padding-left:12px}
  .price i{position:absolute;right:0;top:0;width:35px;height:100%;border-left:1px solid #bfc4c8;display:flex;align-items:center;justify-content:center}
  .more{left:939px;top:660px;font-size:13px;font-weight:300;display:flex;align-items:center;gap:6px}
  .cta{left:494px;top:725px;width:214px;height:39px;background:var(--blue-deep);color:var(--white);font-size:21px;font-weight:500;display:flex;align-items:center;justify-content:center}
  .or{left:0;width:1204px;text-align:center;font-size:12.5px;font-weight:300;color:var(--ink)}
  .site-footer{left:0;top:857px;width:1200px;height:64px;background:var(--footer)}
  .f-link{top:883px;font-size:13px;color:var(--footer-ink)}
  .social{top:878px;width:22px;height:22px;border-radius:50%;background:#7d8184}
</style>
</head>
<body>
  <header class="site-header">
    <div class="abs brand">CARGOWAY</div>
    <svg class="abs" style="left:420px;top:23px" width="21" height="21" viewBox="0 0 21 21"><circle cx="10.5" cy="10.5" r="9" fill="none" stroke="#fff" stroke-width="2"/><circle cx="10.5" cy="10.5" r="4.5" fill="none" stroke="#fff" stroke-width="1.5"/></svg>
    <div class="abs nav-item" style="left:461px">Menu Item 1</div>
    <div class="abs nav-item" style="left:548px">Menu Item 2</div>
    <div class="abs nav-item" style="left:634px">Menu Item 3</div>
    <div class="abs nav-item" style="left:721px">Menu Item 4</div>
    <div class="abs nav-item" style="left:807px">Menu Item 5</div>
    <div class="abs meta" style="left:945px">USD</div>
    <div class="abs meta" style="left:990px">ENGLISH</div>
    <div class="abs user">
      <svg width="14" height="15" viewBox="0 0 14 15"><circle cx="7" cy="4" r="3.6" fill="#fff"/><path d="M0 15c0-5 3-7 7-7s7 2 7 7z" fill="#fff"/></svg>
      DAN HOLLIS
      <svg width="12" height="8" viewBox="0 0 12 8"><path d="M0 1h12L6 7z" fill="#fff"/></svg>
    </div>
  </header>

  <div class="abs hero" role="img" aria-label="Harbour at sunset with cargo cranes and ships reflected in the water"></div>
  <div class="abs hero-title">Search For Quotes</div>
  <div class="abs label-light" style="left:173px;top:184px">Customer</div>
  <div class="abs customer-input"></div>
  <div class="abs check" style="left:171px;top:237px"></div>
  <div class="abs label-light" style="left:193px;top:236px">Rate A Quote ?</div>

  <div class="abs tab active" style="left:498px;top:268px;width:93px;height:79px">
    <svg width="72" height="60" viewBox="0 0 72 60" fill="none" stroke="#fff" stroke-width="5" stroke-linejoin="round"><path d="M36 18 8 10 36 2 64 10z"/><path d="M8 10v30l28 14V18"/><path d="M64 10v30L36 54"/><path d="M8 10 2 22l28 10 6-14M64 10l6 12-28 10-6-14"/></svg>
  </div>
  <div class="abs tab" style="left:597px;top:285px;width:94px;height:62px">
    <svg width="62" height="46" viewBox="0 0 62 46"><g fill="#3a9ad9"><rect x="22" y="14" width="30" height="14" rx="2"/><rect x="10" y="6" width="8" height="20"/><path d="M0 28h62l-8 16H8z"/></g><g fill="#fff"><rect x="26" y="17" width="3" height="9"/><rect x="32" y="17" width="3" height="9"/><rect x="38" y="17" width="3" height="9"/><rect x="44" y="17" width="3" height="9"/><circle cx="16" cy="36" r="2"/><circle cx="24" cy="36" r="2"/><circle cx="32" cy="36" r="2"/></g></svg>
  </div>
  <div class="abs tab" style="left:697px;top:285px;width:93px;height:62px">
    <svg width="46" height="48" viewBox="0 0 46 48"><path d="M23 2 44 12v24L23 46 2 36V12z" fill="#3a9ad9"/><path d="M2 12l21 10 21-10M23 22v24M12 7l21 10M34 7 13 17" stroke="#fff" stroke-width="2.5" fill="none"/></svg>
  </div>

  <section class="abs form-band">
  </section>
  <div class="abs f-label" style="left:172px">Qty</div>
  <div class="abs f-label" style="left:253px">Stackable</div>
  <div class="abs f-label" style="left:341px;top:366px">Load</div>
  <div class="abs f-label" style="left:577px">Length</div>
  <div class="abs f-label" style="left:651px">Width</div>
  <div class="abs f-label" style="left:728px">Height</div>
  <div class="abs f-label" style="left:888px">Weight</div>
  <div class="abs f-input" style="left:170px;width:48px">5</div>
  <div class="abs check" style="left:254px;top:399px"></div>
  <div class="abs f-select" style="left:339px;width:220px">Box / Pallet
    <svg class="abs" style="right:12px;top:10px" width="14" height="8" viewBox="0 0 14 8"><path d="M0 0h14L7 8z" fill="#2b86c5"/></svg>
  </div>
  <div class="abs f-input" style="left:575px;width:59px">100</div>
  <div class="abs f-input" style="left:650px;width:59px">100</div>
  <div class="abs f-input" style="left:724px;width:59px">100</div>
  <div class="abs unit" style="left:791px;width:76px"><span>cm</span><i><svg width="9" height="5" viewBox="0 0 9 5"><path d="M0 0h9L4.5 5z" fill="#fff"/></svg></i></div>
  <div class="abs f-input" style="left:883px;width:59px">100</div>
  <div class="abs unit" style="left:953px;width:78px"><span>kg</span><i><svg width="9" height="5" viewBox="0 0 9 5"><path d="M0 0h9L4.5 5z" fill="#fff"/></svg></i></div>
  <div class="abs add-units">
    <svg width="13" height="13" viewBox="0 0 13 13"><circle cx="6.5" cy="6.5" r="5.7" fill="none" stroke="#fff" stroke-width="1.2"/><path d="M6.5 3.5v6M3.5 6.5h6" stroke="#fff" stroke-width="1.2"/></svg>
    Add more units
  </div>

  <div class="abs route"></div>
  <div class="abs r-label" style="left:170px">From :</div>
  <div class="abs r-input" style="left:213px;width:332px">Shipping address or port</div>
  <svg class="abs" style="left:589px;top:497px" width="22" height="22" viewBox="0 0 22 22"><circle cx="11" cy="11" r="10" fill="none" stroke="#555" stroke-width="1.2"/><path d="M9 6l5 5-5 5" fill="none" stroke="#555" stroke-width="1.2"/></svg>
  <div class="abs r-label" style="left:669px">To :</div>
  <div class="abs r-input" style="left:699px;width:331px">Shipping address or port</div>

  <h2 class="abs options-title" style="font-weight:300">Options</h2>
  <div class="abs opt" style="left:169px">Import</div>
  <div class="abs sep" style="left:223px"></div>
  <div class="abs opt" style="left:237px">Export</div>
  <div class="abs sep" style="left:289px"></div>
  <div class="abs opt" style="left:303px">Incoterm : <a>FCA</a></div>

  <div class="abs check" style="left:487px;top:629px"></div>
  <svg class="abs" style="left:506px;top:624px" width="22" height="22" viewBox="0 0 22 22"><circle cx="11" cy="11" r="9.5" fill="none" stroke="#d7262c" stroke-width="2"/><rect x="7" y="6" width="8" height="10" rx="1" fill="none" stroke="#2b86c5" stroke-width="1.5"/><path d="M4.5 17.5l13-13" stroke="#d7262c" stroke-width="2"/></svg>
  <div class="abs check" style="left:549px;top:629px"></div>
  <svg class="abs" style="left:569px;top:624px" width="22" height="22" viewBox="0 0 22 22"><circle cx="11" cy="11" r="9.5" fill="none" stroke="#d7262c" stroke-width="2"/><circle cx="11" cy="8" r="2" fill="#2b86c5"/><path d="M7 16c1-4 7-4 8 0z" fill="#2b86c5"/><path d="M4.5 17.5l13-13" stroke="#d7262c" stroke-width="2"/></svg>
  <div class="abs check" style="left:609px;top:629px"></div>
  <svg class="abs" style="left:628px;top:624px" width="22" height="22" viewBox="0 0 22 22"><circle cx="11" cy="11" r="9.5" fill="none" stroke="#d7262c" stroke-width="2"/><path d="M11 11 7 6M11 11l5-3M11 11l-1 6M11 11l5 4" stroke="#2b86c5" stroke-width="2.5"/><path d="M4.5 17.5l13-13" stroke="#d7262c" stroke-width="2"/></svg>

  <div class="abs price">Price Level<i><svg width="14" height="7" viewBox="0 0 14 7"><path d="M0 0h14L7 7z" fill="#9a9fa2"/></svg></i></div>
  <div class="abs more">
    <svg width="16" height="16" viewBox="0 0 16 16"><circle cx="8" cy="8" r="7" fill="none" stroke="#777" stroke-width="1.1"/><path d="M8 4.5v7M4.5 8h7" stroke="#777" stroke-width="1.1"/></svg>
    more option
  </div>

  <div class="abs cta">SEARCH QUOTES</div>
  <div class="abs or" style="top:775px">or</div>
  <div class="abs or" style="top:790px;font-size:13.5px">Create manually</div>

  <footer class="abs site-footer"></footer>
  <div class="abs f-link" style="left:171px">About Us</div>
  <div class="abs f-link" style="left:245px">Privacy Policy</div>
  <div class="abs f-link" style="left:350px">Terms Of service</div>
  <div class="abs f-link" style="left:473px">News</div>
  <div class="abs social" style="left:881px"></div>
  <div class="abs social" style="left:913px"></div>
  <div class="abs social" style="left:944px"></div>
  <div class="abs social" style="left:975px"></div>
  <div class="abs social" style="left:1007px"></div>
</body>
</html>
```